New logo and wordpress design for Scholar-pathways.net

We run a website that collates profiles/interviews of individuals who have completed a PhD and moved away from a traditional academix career path into something related. This is often related to the field they studied in, such as publishing, government policy, consulting, teaching and many other things. The website https://scholar-pathways.net aims to give students and researchers ideas about what paths they can take their career on.

We would like to refresh our brand with a new website and logo. Our website is run through wordpress and hence we would need appropriate files and designs to accomodate this.
Our new logo should represent the idea of navigating a career path and exploring the unknown. Up until now it has been a compass in tones of purple and blue. We are happy to keep this motif but would need an updated, more representative logo. We are also happy to get some new ideas if the designer has something they think would fit.
The website itself should have fresh and clean look. We would like a banner at the top with clear links to the various parts of the site. The banner should stay consistent throughout the site.
We would like the main page to have a clean and simple look which places the focus on the profiles and their associated photos.
We would like pictographs to represent the different fields which our profiles fit into and would like to discuss with the winning designer what these would look like exactly. As a starting point we would like pictographs representing STEM (Science, Technology, Engineering, Mathematics) and SHAPE (Social Sciences, Humanities and Arts for People and the Economy).
Updates

We are really looking for something that is clean and professional but embodies our mission to represent all of the major industries which doctoral graduates can go on to work in. Those being, academia (universities), government, industry (private enterprise and companies), and third sector (Charities and think tanks etc.). Any design should cover all of these and not focus just on a big business or similar. It should also represent that we are not purely science focused, but all disciplines and are a broad church in that sense. We are open to various colour schemes and ideas but would like something that gives a professional but approachable feel, it should have elements of Fenwick, but not suggest that we are only open to Fenwick University students or graduates.
Some sites that may be useful are:
https://lumenguild.net/news-resources/projects/research-culture/ - talks about the different areas of employment we are trying to represent
https://www.humstud.fw.ac.uk/ an fenwick internal website that we like the presentation of.

Target Market(s)

Academic researchers with a PhD

Industry/Entity Type

Academic Careers

Colors
0054AA
0677BA
7BADD7
CADEEF
E8F1F8
00AB8E
00BBA5
67D7C9
C6EFE9
E9F9F6
FFF300
FFF600
FEFA6F
FFFEC7
FFFEE8
6B429C
8869AF
B7A5CE
E3DAEB
F3F0F8

Requirements
Must have
• A new logo
Should not have
• The existing logo

```html
<!DOCTYPE html>
<html lang="en">
<head>
<meta charset="utf-8">
<title>Scholar Pathways – Explore Your Options Beyond Academia</title>
<link href="https://fonts.googleapis.com/css2?family=Poppins:wght@300;400;500;600&display=swap" rel="stylesheet">
<style>
:root{
  --blue:#0054AA;
  --blue-mid:#0677BA;
  --blue-soft:#7BADD7;
  --blue-pale:#CADEEF;
  --blue-wash:#E8F1F8;
  --teal:#00AB8E;
  --teal-pale:#C6EFE9;
  --purple:#6B429C;
  --purple-pale:#E3DAEB;
  --ink:#111418;
  --text:#4a4f57;
  --muted:#6b7079;
  --footer:#0d0d0f;
  --white:#ffffff;
}
*{box-sizing:border-box;margin:0;padding:0}
html,body{width:1200px;height:4001px;overflow:hidden}
body{font-family:'Poppins',sans-serif;color:var(--ink);background:var(--white);position:relative}
.page{position:relative;width:1200px;height:4001px;overflow:hidden}
.abs{position:absolute}

/* hero */
.hero-bg{left:0;top:0;width:1200px;height:680px;background:linear-gradient(180deg,#c9dcef 0%,#e3eef8 55%,#ffffff 100%)}
.brand{display:flex;align-items:center;gap:10px;font-size:12px;font-weight:500;line-height:15px;color:#10224a}
.brand-dot{width:20px;height:20px;border-radius:50%;background:var(--blue)}
.nav{left:498px;top:39px;display:flex;align-items:center;font-size:12.5px;color:#1d2430}
.nav a{text-decoration:none;color:inherit}
.nav .home{background:var(--blue);color:#fff;font-weight:600;border-radius:20px;width:86px;height:34px;display:flex;align-items:center;justify-content:center;margin-right:34px}
.nav .link{margin-right:33px}
.hero-title{left:92px;top:148px;font-size:56px;font-weight:500;line-height:70px;letter-spacing:.3px}
.hero-title em{font-style:normal;color:var(--blue)}
.hero-lead{left:92px;top:372px;width:450px;font-size:20px;line-height:33px;color:var(--muted);font-weight:400}
.btn{display:inline-flex;align-items:center;background:var(--blue);color:#fff;border-radius:40px;font-weight:400;text-decoration:none}
.btn .arrow{border-radius:50%;background:rgba(255,255,255,.18);display:flex;align-items:center;justify-content:center}
.btn-lg{left:92px;top:506px;height:62px;width:268px;padding-left:25px;font-size:21px;gap:0;justify-content:space-between;padding-right:16px}
.btn-lg .arrow{width:36px;height:36px}
.btn-sm{height:45px;font-size:14px;padding:0 12px 0 21px;gap:16px}
.btn-sm .arrow{width:27px;height:27px}
.hero-photo{left:652px;top:105px;width:443px;height:513px;border-radius:110px 110px 190px 190px / 90px 90px 160px 160px;background:linear-gradient(180deg,#9fc2e6 0%,#6e9fd3 60%,#5b8ec8 100%)}
.card-float{background:#fff;border-radius:10px;box-shadow:0 8px 24px rgba(20,50,90,.12)}
.success{left:967px;top:180px;width:171px;height:79px;display:flex;align-items:center;gap:14px;padding-left:18px}
.success .badge{width:42px;height:42px;border-radius:50%;background:var(--blue-mid);box-shadow:0 0 0 5px var(--blue-pale)}
.success small{display:block;font-size:11px;color:#333}
.success strong{font-size:27px;font-weight:600;line-height:30px}
.partners{left:616px;top:480px;width:169px;height:76px;padding:12px 16px}
.partners p{font-size:11px;color:#222;margin-bottom:8px}
.avatars{display:flex}
.avatars span{width:27px;height:27px;border-radius:50%;border:2px solid #fff;margin-right:-8px}
.avatars .more{background:var(--blue);color:#fff;font-size:8px;font-weight:600;display:flex;align-items:center;justify-content:center}

/* feature sections */
.panel{background:var(--blue-pale);border-radius:14px}
.photo{border-radius:14px}
.eyebrow{display:flex;align-items:center;gap:26px;color:var(--blue);font-size:20px;font-weight:400}
.eyebrow::before{content:"";width:40px;height:2px;background:var(--blue)}
.sec-title{font-size:36px;font-weight:500;line-height:50px}
.sec-text{font-size:13.5px;line-height:21.7px;color:var(--muted);text-align:justify}

/* profiles */
.profiles-title{left:0;top:2084px;width:1200px;text-align:center;font-size:36px;font-weight:500}
.grid{left:92px;top:2164px;width:1016px;display:grid;grid-template-columns:repeat(3,316px);column-gap:34px;row-gap:42px}
.profile-photo{height:332px;border-radius:14px;position:relative}
.tags{position:absolute;left:12px;top:12px;display:flex;gap:8px}
.tag{display:flex;align-items:center;gap:7px;background:rgba(255,255,255,.82);border-radius:14px;padding:4px 11px 4px 5px;font-size:12px}
.tag i{width:17px;height:17px;border-radius:50%}
.tag.stem{color:var(--teal)} .tag.stem i{background:var(--teal-pale)}
.tag.shape{color:var(--purple)} .tag.shape i{background:var(--purple-pale)}
.profile h3{font-size:21px;font-weight:500;margin-top:26px;line-height:28px}
.profile .role{font-size:13px;color:var(--muted);line-height:21px;margin-top:2px}
.profile .bio{font-size:12px;line-height:20px;color:#222;text-align:justify;margin-top:12px}
.meta{display:grid;grid-template-columns:116px 1fr;margin-top:24px;row-gap:12px}
.meta dt{font-size:9px;color:var(--blue-mid);line-height:12px}
.meta dd{font-size:12px;color:#222;line-height:18px}
.meta .full{grid-column:1/3}
.rule{left:92px;top:3472px;width:1016px;height:1px;background:#e2e5ea}
.pager{left:92px;top:3490px}
.page-count{right:92px;top:3501px;font-size:15px;color:var(--muted)}

/* footer */
.footer{left:0;top:3610px;width:1200px;height:391px;background:var(--footer);color:#fff}
.footer .brand{position:absolute;left:92px;top:62px;color:#fff;font-size:11px;line-height:14px}
.footer .about{position:absolute;left:92px;top:117px;width:266px;font-size:12px;line-height:20px;color:#cfd2d6;text-align:justify}
.fcol{position:absolute;font-size:12px}
.fcol h4{font-size:15px;font-weight:500;margin-bottom:10px}
.fcol li{list-style:none;line-height:21.7px;color:#e5e7ea}
.socials{display:flex;gap:7px;margin-top:6px}
.socials span{width:24px;height:24px;border-radius:50%;background:var(--blue-mid)}
.contact{position:absolute;left:798px;top:37px;width:310px}
.contact h4{font-size:15px;font-weight:500;margin-bottom:12px}
.field{background:#fff;border-radius:5px;height:40px;margin-bottom:11px;font-size:11px;color:#b3b6bb;padding:12px 15px}
.field.msg{height:85px}
.send{width:97px;height:30px;border-radius:4px;background:var(--blue);color:#fff;font-size:11px;display:flex;align-items:center;justify-content:center;margin-top:3px}
.footer .line{position:absolute;left:92px;top:334px;width:1016px;height:1px;background:#3a3d42}
.copy{position:absolute;left:0;top:352px;width:1200px;text-align:center;font-size:11px;color:#cfd2d6}
</style>
</head>
<body>
<div class="page">

  <!-- header & hero -->
  <div class="abs hero-bg"></div>
  <div class="abs brand" style="left:96px;top:41px"><span class="brand-dot"></span><span>Scholar<br>Pathways</span></div>
  <nav class="abs nav">
    <a class="home" href="#">Home</a>
    <a class="link" href="#">Career profiles</a>
    <a class="link" href="#">Get involved</a>
    <a class="link" href="#">Events</a>
    <a class="link" href="#">Resources</a>
    <a class="link" href="#">About us</a>
    <svg width="15" height="15" viewBox="0 0 16 16" fill="none" stroke="#1d2430" stroke-width="1.8" style="margin-left:40px"><circle cx="7" cy="7" r="5"/><path d="M11 11l4 4"/></svg>
  </nav>

  <h1 class="abs hero-title">Explore Your<br>Options <em>Beyond</em><br>Academia</h1>
  <p class="abs hero-lead">A collection of profiles of people who have made the transition from academia to industry</p>
  <a class="abs btn btn-lg" href="#">Get started today <span class="arrow"><svg width="16" height="16" viewBox="0 0 16 16" fill="none" stroke="#fff" stroke-width="1.8"><path d="M3 8h10M9 4l4 4-4 4"/></svg></span></a>

  <div class="abs hero-photo" role="img" aria-label="Smiling young professional in a dark suit celebrating with raised fists against a blue shape"></div>
  <div class="abs card-float success"><span class="badge"></span><div><small>Success Rate</small><strong>95%</strong></div></div>
  <div class="abs card-float partners"><p>Our Partners</p>
    <div class="avatars"><span style="background:#8a8f96"></span><span style="background:#b59a84"></span><span style="background:#5f6670"></span><span style="background:#3f444b"></span><span style="background:#9a8f86"></span><span class="more">1K+</span></div>
  </div>

  <!-- about -->
  <div class="abs panel" style="left:116px;top:753px;width:450px;height:352px"></div>
  <div class="abs photo" style="left:92px;top:726px;width:447px;height:350px;background:linear-gradient(180deg,#7fa9d6 0%,#b9cde0 40%,#8e8a72 70%,#5e7c4a 100%)" role="img" aria-label="Domed university library and historic college rooftops under a blue sky"></div>
  <div class="abs eyebrow" style="left:633px;top:786px">About Us</div>
  <h2 class="abs sec-title" style="left:633px;top:823px">Our Mission and Team</h2>
  <p class="abs sec-text" style="left:633px;top:886px;width:475px">Scholar Pathways is edited by a group of DPhil students and researchers connected to Fenwick University. Our aim is to provide a platform that showcases diverse career paths for PhD graduates and offers practical advice for transitioning from academia to industry.</p>
  <a class="abs btn btn-sm" href="#" style="left:633px;top:998px">Learn more <span class="arrow"><svg width="13" height="13" viewBox="0 0 16 16" fill="none" stroke="#fff" stroke-width="1.8"><path d="M3 8h10M9 4l4 4-4 4"/></svg></span></a>

  <!-- career profiles -->
  <div class="abs eyebrow" style="left:92px;top:1191px">Career Profiles</div>
  <h2 class="abs sec-title" style="left:92px;top:1229px;width:480px">Real Stories from PhD<br>Graduates</h2>
  <p class="abs sec-text" style="left:92px;top:1343px;width:474px">Dive into our extensive collection of career profiles featuring researchers who have ventured into industries such as publishing, government policy, consulting, teaching, and more. Each profile provides a detailed account of their transition, the skills they found valuable, and the challenges they overcame. Learn from their experiences and find inspiration for your own career path.</p>
  <a class="abs btn btn-sm" href="#" style="left:92px;top:1498px">Explore profiles <span class="arrow"><svg width="13" height="13" viewBox="0 0 16 16" fill="none" stroke="#fff" stroke-width="1.8"><path d="M3 8h10M9 4l4 4-4 4"/></svg></span></a>
  <div class="abs panel" style="left:660px;top:1207px;width:448px;height:350px"></div>
  <div class="abs photo" style="left:633px;top:1180px;width:447px;height:349px;background:linear-gradient(135deg,#b9c6d0 0%,#8b97a3 45%,#6f6a63 75%,#b9a184 100%)" role="img" aria-label="Smiling professional holding a tablet in front of a team of industrial workers"></div>

  <!-- get involved -->
  <div class="abs panel" style="left:120px;top:1658px;width:446px;height:350px"></div>
  <div class="abs photo" style="left:92px;top:1631px;width:447px;height:349px;background:linear-gradient(135deg,#c9b9a3 0%,#a7b3b7 45%,#e6e4de 75%,#8f8a80 100%)" role="img" aria-label="Smiling woman working on a laptop in a bright office"></div>
  <div class="abs eyebrow" style="left:633px;top:1691px">Get Involved</div>
  <h2 class="abs sec-title" style="left:633px;top:1729px">Join Our Community</h2>
  <p class="abs sec-text" style="left:633px;top:1792px;width:475px">Are you interested in contributing to the Scholar Pathways project? We welcome PhD graduates and researchers to share their career stories, participate in events, and help us expand our collection of profiles. Your experiences can inspire and guide the next generation of researchers.</p>
  <a class="abs btn btn-sm" href="#" style="left:633px;top:1904px">Contribute your story <span class="arrow"><svg width="13" height="13" viewBox="0 0 16 16" fill="none" stroke="#fff" stroke-width="1.8"><path d="M3 8h10M9 4l4 4-4 4"/></svg></span></a>

  <!-- recent profiles -->
  <h2 class="abs profiles-title">Recent Profiles</h2>
  <div class="abs grid">
    <article class="profile">
      <div class="profile-photo" style="background:linear-gradient(160deg,#d8d6d2 0%,#9c8e82 50%,#4a3a32 100%)" role="img" aria-label="Portrait of a woman with long curly hair"><div class="tags"><span class="tag shape"><i></i>Psychology</span></div></div>
      <h3>Marisol Ortega-Lind</h3>
      <p class="role">Behavioural Scientist at Brightwell</p>
      <p class="bio">In 2019, I joined the Nudge Lab Partnership (NLP) as an advisor and led over 25 research projects aimed at enhancing the design of products, services, policies, and communications using behavioural science.</p>
      <dl class="meta"><div><dt>Career Profiles</dt><dd>PHD</dd></div><div><dt>Left Academia After</dt><dd>6+ Years Postdoc</dd></div><div class="full"><dt>Sector</dt><dd>Charities, Uncategorized</dd></div></dl>
    </article>
    <article class="profile">
      <div class="profile-photo" style="background:linear-gradient(180deg,#f2f2f2 0%,#e6e6e6 55%,#3d4d5c 100%)" role="img" aria-label="Portrait of a man in a dark t-shirt on a white background"><div class="tags"><span class="tag stem"><i></i>Molecular</span><span class="tag stem"><i></i>Genetics</span></div></div>
      <h3>Nikos Varelas</h3>
      <p class="role">Senior Scientist at Calyx Bio</p>
      <p class="bio">Academia, in most cases, prepares you well to take on most tasks. The only requirement is to adapt to a more commercially focused environment and apply those same skills in more flexible ways.</p>
      <dl class="meta"><div><dt>Career Profiles</dt><dd>PHD</dd></div><div><dt>Left Academia After</dt><dd>0-3 Years Postdoc</dd></div><div class="full"><dt>Sector</dt><dd>Biotech</dd></div></dl>
    </article>
    <article class="profile">
      <div class="profile-photo" style="background:linear-gradient(135deg,#c7d2d8 0%,#e8e2de 45%,#d9a6ac 75%,#f0ece8 100%)" role="img" aria-label="Portrait of a woman with pink hair in a laboratory"><div class="tags"><span class="tag stem"><i></i>Biology</span></div></div>
      <h3>Clara Whitfield</h3>
      <p class="role">Research Advisor at Women's Cancer Research Trust (WCRT)</p>
      <p class="bio">I completed a Bachelor of Science (Medical Bioscience), then an Honours degree in ovarian cancer biology.</p>
      <dl class="meta"><div><dt>Career Profiles</dt><dd>PHD</dd></div><div><dt>Left Academia After</dt><dd>0-3 Years Postdoc</dd></div><div class="full"><dt>Sector</dt><dd>Charities, Public Health</dd></div></dl>
    </article>
    <article class="profile">
      <div class="profile-photo" style="background:linear-gradient(160deg,#b6a6c8 0%,#7d8a6c 45%,#2e3550 100%)" role="img" aria-label="Portrait of a woman with dark hair in front of purple flowers"><div class="tags"><span class="tag stem"><i></i>Biochemistry</span></div></div>
      <h3>Rana Haddad</h3>
      <p class="role">Assistant Director- Analytics &amp; Modeling - Event Response at Meridian Risk</p>
      <p class="bio">Working on current events which are shaping our world, exposure to a variety of natural perils, requirement of problem solving and coding experience.</p>
      <dl class="meta"><div><dt>Career Profiles</dt><dd>PHD</dd></div><div><dt>Left Academia After</dt><dd>0-3 Years Postdoc</dd></div><div class="full"><dt>Sector</dt><dd>Consulting</dd></div></dl>
    </article>
    <article class="profile">
      <div class="profile-photo" style="background:linear-gradient(180deg,#5c7fa3 0%,#3f6d96 50%,#8b8478 80%,#e6e2da 100%)" role="img" aria-label="Portrait of a woman wearing glasses beside a lake"><div class="tags"><span class="tag stem"><i></i>Biochemistry</span></div></div>
      <h3>Meera Kapadia</h3>
      <p class="role">Consultant at Independent/Freelance</p>
      <p class="bio">I specialize in collaborating with educational institutions and museums, providing expert consultation on developing and enhancing their science and sustainability programs.</p>
      <dl class="meta"><div><dt>Career Profiles</dt><dd>PHD</dd></div><div><dt>Left Academia After</dt><dd>3-6 Years Postdoc</dd></div><div class="full"><dt>Sector</dt><dd>Education, Museum, Sustainable Development Communication</dd></div></dl>
    </article>
    <article class="profile">
      <div class="profile-photo" style="background:linear-gradient(180deg,#f1e3da 0%,#e8d6cc 55%,#d39aa0 100%)" role="img" aria-label="Portrait of a woman in a floral top against a light background"><div class="tags"><span class="tag stem"><i></i>Molecular</span><span class="tag stem"><i></i>Biology</span></div></div>
      <h3>Tara Sen</h3>
      <p class="role">Visual Science Communicator at Tarasketch</p>
      <p class="bio">Left academia after Ph.D. I started freelancing a few months after the submission of my PhD thesis. I did pursue a postdoctoral fellowship, where I was on a drawing board and not on the bench.</p>
      <dl class="meta"><div><dt>Career Profiles</dt><dd>PHD</dd></div><div><dt>Left Academia After</dt><dd>0-3 Years Postdoc</dd></div><div class="full"><dt>Sector</dt><dd>Freelance, Science Communications, Scientific Illustration</dd></div></dl>
    </article>
  </div>

  <div class="abs rule"></div>
  <a class="abs btn btn-sm pager" href="#">Next page <span class="arrow"><svg width="13" height="13" viewBox="0 0 16 16" fill="none" stroke="#fff" stroke-width="1.8"><path d="M3 8h10M9 4l4 4-4 4"/></svg></span></a>
  <p class="abs page-count">Page 1 of 10</p>

  <!-- footer -->
  <footer class="abs footer">
    <div class="brand"><span class="brand-dot"></span><span>Scholar<br>Pathways</span></div>
    <p class="about">We, the editors, are a team of curious and committed volunteer PhD students and research staff working in partnership with the University of Fenwick's Careers Service. Our role is to source career profiles from a range of fascinating sectors written by researchers with backgrounds spanning the humanities, social sciences, physical and life sciences.</p>
    <div class="fcol" style="left:436px;top:48px"><h4>Quick Links</h4><ul><li>Home</li><li>Career Profiles</li><li>Get Involved</li><li>Events</li><li>Resources</li><li>About Us</li></ul></div>
    <div class="fcol" style="left:599px;top:48px"><h4>Company</h4><ul><li>Support</li><li>Privacy Policy</li><li>Term &amp; Conditions</li></ul>
      <h4 style="margin-top:22px">Stay Connected</h4><div class="socials"><span></span><span></span><span></span></div></div>
    <div class="contact"><h4>Contact Us For the Further Information</h4>
      <div class="field">Write your name</div><div class="field">Write your email</div><div class="field msg">Write your message</div>
      <div class="send">Send</div></div>
    <div class="line"></div>
    <p class="copy">© 2024 Scholar Pathways – All rights reserved.</p>
  </footer>
</div>
</body>
</html>
```